Maple Hollow Bloom Panels Business card

Looking to have a business card design incorporating my logo for my flower wall business.

Industry/Entity Type

Wedding & event planning

Contact Information for Business Card

My business logo, my name - Lena Whitcombe (owner), my tagline - Let us be your something extra, phone # 401-726-3148, email address - maplehollowbloompanels@mailvane.net, my website - maplehollowbloompanels.net, Instagram handle- @maplehollowbloompanels, FB handle Handle - maplehollowbloompanels

Font styles to use
Other font styles liked:
• Sentaina is the font that is used in my logo

Requirements
Must have
• Would like a double sided business card

```html
<!DOCTYPE html>
<html lang="en">
<head>
<meta charset="utf-8">
<title>Maple Hollow Bloom Panels – Business Card</title>
<link href="https://fonts.googleapis.com/css2?family=Montserrat:wght@300;400;600&display=swap" rel="stylesheet">
<style>
  :root {
    --backdrop: #d6d6d6;
    --card-white: #ffffff;
    --blush: #f9dce8;
    --magenta: #c8197f;
    --ink: #2e2e2e;
    --gold: #d6b24a;
  }
  html, body {
    margin: 0;
    padding: 0;
    width: 1200px;
    height: 965px;
    overflow: hidden;
    background: var(--backdrop);
    font-family: "Montserrat", Arial, sans-serif;
  }
  .canvas { position: relative; width: 1200px; height: 965px; }
  .card {
    position: absolute;
    top: 159px;
    width: 383px;
    height: 669px;
    border-radius: 40px;
    overflow: hidden;
  }
  .card--front { left: 186px; background: var(--card-white); }
  .card--back { left: 653px; background: var(--blush); }

  .brand-mark {
    position: absolute;
    border-radius: 50%;
    display: flex;
    align-items: center;
    justify-content: center;
    text-align: center;
    box-sizing: border-box;
  }
  .card--front .brand-mark {
    left: 74px; top: 75px; width: 236px; height: 236px;
    border: 1.5px solid var(--gold);
  }
  .card--back .brand-backing {
    position: absolute;
    left: 50px; top: 74px; width: 282px; height: 282px;
    border-radius: 50%;
    background: var(--card-white);
  }
  .card--back .brand-mark {
    left: 66px; top: 90px; width: 250px; height: 250px;
    border: 1.5px solid var(--gold);
  }
  .brand-name {
    font-weight: 400;
    font-size: 22px;
    line-height: 1.35;
    color: var(--ink);
    letter-spacing: 0.5px;
    width: 170px;
  }

  .owner {
    position: absolute;
    left: 38px; top: 400px;
    margin: 0;
    font-weight: 400;
    font-size: 23px;
    line-height: 1.2;
    color: var(--magenta);
    white-space: nowrap;
  }
  .owner .role { font-size: 15px; color: var(--ink); margin-left: 6px; }

  .contact-group {
    position: absolute;
    left: 32px;
    display: grid;
    grid-template-columns: 14px 1px auto;
    column-gap: 14px;
    row-gap: 6px;
    align-items: center;
  }
  .contact-group--social { top: 460px; }
  .contact-group--direct { top: 534px; }
  .contact-group .divider {
    grid-column: 2;
    grid-row: 1 / span 2;
    width: 1px;
    align-self: stretch;
    background: #bbb;
  }
  .contact-group .icon { grid-column: 1; display: flex; justify-content: center; }
  .contact-group .value {
    grid-column: 3;
    font-weight: 300;
    font-size: 14px;
    line-height: 17px;
    color: var(--ink);
    white-space: nowrap;
  }
  .icon .dot { width: 8px; height: 8px; border-radius: 50%; background: var(--magenta); }
  .icon .square { width: 8px; height: 8px; border: 1.3px solid var(--magenta); border-radius: 2px; }

  .web-band {
    position: absolute;
    left: 0; top: 607px;
    width: 100%; height: 33px;
    background: var(--blush);
    display: flex; align-items: center; justify-content: center;
    font-size: 15px; font-weight: 400; color: var(--magenta);
  }
  .web-band strong { font-weight: 600; }

  .tagline-band {
    position: absolute;
    left: 0; top: 536px;
    margin: 0;
    width: 100%; height: 67px;
    background: var(--card-white);
    display: flex; align-items: center; justify-content: center;
    text-align: center;
    font-size: 21px; font-weight: 400; line-height: 1.15;
    color: var(--magenta);
    letter-spacing: 0.5px;
  }
</style>
</head>
<body>
<main class="canvas">

  <section class="card card--front" aria-label="Card front">
    <div class="brand-mark">
      <span class="brand-name">Maple Hollow Bloom Panels</span>
    </div>

    <h1 class="owner">Lena Whitcombe<span class="role">owner</span></h1>

    <div class="contact-group contact-group--social">
      <span class="icon" style="grid-row:1"><span class="dot"></span></span>
      <span class="divider"></span>
      <span class="value" style="grid-row:1">@maplehollowbloompanels</span>
      <span class="icon" style="grid-row:2"><span class="square"></span></span>
      <span class="value" style="grid-row:2">maplehollowbloompanels</span>
    </div>

    <div class="contact-group contact-group--direct">
      <span class="icon" style="grid-row:1">
        <svg width="12" height="14" viewBox="0 0 12 14" aria-hidden="true">
          <path d="M3 1 L5 4 L3.6 5.4 Q5 9 8 10.6 L9.4 9.2 L11.5 11.5 L9.8 13 Q4 12 1.5 3 Z" fill="none" stroke="var(--magenta)" stroke-width="1.3" stroke-linejoin="round"/>
        </svg>
      </span>
      <span class="divider"></span>
      <span class="value" style="grid-row:1">401-726-3148</span>
      <span class="icon" style="grid-row:2">
        <svg width="13" height="10" viewBox="0 0 13 10" aria-hidden="true">
          <rect x="0.7" y="0.7" width="11.6" height="8.6" rx="1" fill="none" stroke="var(--magenta)" stroke-width="1.3"/>
          <path d="M1 1.2 L6.5 5.5 L12 1.2" fill="none" stroke="var(--magenta)" stroke-width="1.3"/>
        </svg>
      </span>
      <span class="value" style="grid-row:2">maplehollowbloompanels@mailvane.net</span>
    </div>

    <div class="web-band">www.<strong>maplehollowbloompanels</strong>.net</div>
  </section>

  <section class="card card--back" aria-label="Card back">
    <div class="brand-backing"></div>
    <div class="brand-mark">
      <span class="brand-name">Maple Hollow Bloom Panels</span>
    </div>
    <p class="tagline-band">Let us be<br>your something extra</p>
  </section>

</main>
</body>
</html>
```